TMVB site redesign

Please redesign a home page with content provided. PSD only - no coding
Can use any images from pexorama.example

Please create a site design that more clearly illustrates the client's services and expertise. We are looking for a high-end design.

Any images used must be generic or of Dallas TX.

Fonts: Any
Colors: Match to logo
Look: Modern - Professional

Target Market(s)

medium-large business owners

Number of Pages Required

1 page

Font styles to use
Serif
Sans Serif

Requirements
Must have
• cohesive professional design
• high end look
• Match to logo

```html
<!DOCTYPE html>
<html lang="en">
<head>
<meta charset="utf-8">
<title>TMVB – Tenant Representation</title>
<link rel="stylesheet" href="https://fonts.googleapis.com/css2?family=Poppins:ital,wght@0,400;0,500;0,600;0,700;1,400&family=Open+Sans:ital,wght@0,400;0,600;1,400&display=swap">
<style>
:root{
  --red:#d8413a;
  --red-dark:#b9302b;
  --red-soft:#e4605a;
  --ink:#2a2a2a;
  --muted:#6b6b6b;
  --line:#e2e2e2;
  --white:#ffffff;
  --sky:#cfdbe6;
}
*{box-sizing:border-box;margin:0;padding:0}
html,body{width:1200px;height:3226px;overflow:hidden}
body{position:relative;background:var(--white);font-family:"Open Sans",Arial,sans-serif;color:var(--ink)}
.abs{position:absolute}
h2.section-title{position:absolute;left:0;width:1200px;text-align:center;font:600 14px "Poppins",sans-serif;letter-spacing:.5px;color:var(--ink);text-transform:uppercase}
h2.section-title span{color:var(--red)}

/* header */
.site-header{position:absolute;top:0;left:0;width:1200px;height:90px;background:var(--white)}
.brand{position:absolute;left:132px;top:12px;width:130px;text-align:center}
.brand-mark{display:inline-block;background:var(--red);color:var(--white);font:600 22px "Poppins",sans-serif;padding:2px 12px;letter-spacing:1px}
.brand-name{font:500 10px "Poppins",sans-serif;color:var(--ink);margin-top:4px;letter-spacing:.8px;text-transform:uppercase}
.main-nav{position:absolute;left:405px;top:40px;display:flex;gap:27px;font:600 11px "Poppins",sans-serif;color:var(--ink)}
.call-btn{position:absolute;left:898px;top:27px;width:172px;height:40px;border-radius:20px;background:var(--red);color:var(--white);padding:5px 0 0 24px;font-family:"Poppins",sans-serif}
.call-btn small{display:block;font-size:9px;line-height:10px}
.call-btn b{font-size:17px;font-weight:700;line-height:20px}

/* hero */
.hero{position:absolute;top:90px;left:0;width:1200px;height:482px;background:linear-gradient(180deg,#2f7fd0 0%,#6fb1e8 40%,#8fb6c8 62%,#5f8f3f 78%,#3e6e2a 100%)}
.hero h1{position:absolute;left:140px;top:150px;width:520px;font:700 33px/40px "Poppins",sans-serif;color:var(--white);text-transform:uppercase}
.hero p{position:absolute;left:140px;top:233px;width:370px;font:400 12px/20px "Open Sans",sans-serif;color:var(--white)}
.hero .btn{position:absolute;left:140px;top:290px;width:115px;height:26px;border-radius:13px;background:var(--red);color:var(--white);font:600 9px/26px "Poppins",sans-serif;text-align:center}
.hero .arrow{position:absolute;top:212px;width:30px;height:30px;border-radius:50%;background:rgba(255,255,255,.35)}

/* features */
.feature{position:absolute;width:260px;text-align:center}
.feature .ico{width:46px;height:46px;margin:0 auto;border:1.5px solid var(--red);border-radius:50%;display:flex;align-items:center;justify-content:center}
.feature h3{font:600 11px "Poppins",sans-serif;margin-top:12px;text-transform:uppercase}
.feature p{font:400 10.5px/18px "Open Sans",sans-serif;color:var(--muted);margin-top:8px}
.house-photo{position:absolute;left:760px;top:700px;width:230px;height:275px;background:linear-gradient(180deg,#dfe8f0,#b9c2c7 55%,#4f7a3c)}
.house-side{position:absolute;background:linear-gradient(180deg,#e8ecef,#9aa39a)}
.house-frame{position:absolute;left:780px;top:684px;width:205px;height:278px;border:4px solid var(--red)}

/* red bands */
.band{position:absolute;left:133px;width:934px;background:linear-gradient(180deg,#e35f55,#cf3a33);color:var(--white);border-radius:60px 0 60px 0;overflow:hidden}
.band .inner-frame{position:absolute;left:25px;top:25px;right:25px;bottom:25px;border:1px solid rgba(255,255,255,.35);border-radius:45px 0 45px 0}
.band-cta{top:1040px;height:253px;text-align:center}
.band-cta p{position:absolute;top:72px;left:0;width:100%;font:400 14px/28px "Poppins",sans-serif}
.band-cta .btn{position:absolute;left:370px;top:148px;width:195px;height:40px;border-radius:20px;background:var(--white);color:var(--ink);font:600 13px/40px "Poppins",sans-serif}

/* team */
.intro{position:absolute;left:205px;top:1358px;width:790px;text-align:center;font:400 11.5px/21px "Open Sans",sans-serif;color:var(--muted)}
.member{position:absolute;top:1470px;width:272px;text-align:center}
.member .photo{height:232px;border-radius:40px 0 40px 0}
.member h4{font:600 11px "Poppins",sans-serif;margin-top:14px}
.member em{display:block;font:italic 400 10px "Open Sans",sans-serif;color:var(--muted);margin-top:4px}

/* testimonial */
.band-quote{top:1800px;height:365px;text-align:center}
.band-quote .kicker{position:absolute;top:56px;width:100%;font:400 11px "Poppins",sans-serif}
.band-quote h3{position:absolute;top:78px;width:100%;font:600 15px "Poppins",sans-serif}
.band-quote .avatar{position:absolute;left:352px;top:120px;width:86px;height:76px;background:linear-gradient(180deg,#e9e2d6,#9aa3a8);border:3px solid var(--white)}
.band-quote .who{position:absolute;left:452px;top:148px;text-align:left;font:500 12px "Poppins",sans-serif}
.band-quote .who small{display:block;font-size:9px;margin-top:3px}
.band-quote blockquote{position:absolute;left:120px;top:218px;width:694px;font:italic 400 11.5px/25px "Open Sans",sans-serif}
.dots{position:absolute;top:320px;left:0;width:100%;display:flex;justify-content:center;gap:12px}
.dots i{width:5px;height:5px;border-radius:50%;background:rgba(255,255,255,.6)}
.dots i:first-child{background:var(--white)}

/* appointment */
.appt{position:absolute;left:160px;top:2230px;width:550px;text-align:right;font:600 15px/24px "Poppins",sans-serif;color:var(--ink)}
.appt-btn{position:absolute;left:762px;top:2232px;width:253px;height:46px;border-radius:23px;background:var(--red);color:var(--white);font:600 13px/46px "Poppins",sans-serif;text-align:center}

/* articles */
.article{position:absolute;top:2400px;width:285px}
.article .thumb{height:175px;border-radius:30px 0 30px 0}
.article h5{font:600 10.5px "Poppins",sans-serif;margin-top:16px}
.article p{font:400 10.5px/18px "Open Sans",sans-serif;color:var(--muted);margin-top:6px}
.article a{font:400 10px "Open Sans",sans-serif;color:var(--red);text-decoration:underline}

/* footer */
.skyline-fade{position:absolute;left:0;top:2700px;width:1200px;height:526px;background:linear-gradient(180deg,rgba(255,255,255,0),rgba(207,219,230,.45) 70%,rgba(190,205,218,.55))}
.find h3,.contact h3,.social h3{font:600 14px "Poppins",sans-serif;text-transform:uppercase}
.find h3 span,.contact h3 span,.social h3 span{color:var(--red)}
.find{position:absolute;left:132px;top:2750px;width:400px}
.find p{font:400 11px/21px "Open Sans",sans-serif;color:var(--muted);margin-top:12px}
.info{position:absolute;left:132px;display:flex;align-items:center;gap:18px;font:400 11px/20px "Open Sans",sans-serif;color:var(--muted)}
.info .dot{width:40px;height:40px;border-radius:50%;background:var(--red);display:flex;align-items:center;justify-content:center}
.notices{position:absolute;left:145px;top:3080px;font:400 9.5px/20px "Open Sans",sans-serif;color:var(--ink)}
.notices li{list-style:none}
.notices li.sub{padding-left:6px;text-decoration:underline;color:var(--muted)}
.notices b{color:var(--red)}
.contact{position:absolute;left:612px;top:2750px;width:455px}
.field{position:absolute;background:var(--white);border:1px solid var(--line);font:400 10px "Open Sans",sans-serif;color:#aaa;padding:12px 14px}
.send{position:absolute;left:612px;top:3005px;width:78px;height:34px;background:var(--red);color:var(--white);font:600 10px/34px "Poppins",sans-serif;text-align:center}
.social{position:absolute;left:612px;top:3075px}
.social .icons{display:flex;gap:8px;margin-top:14px}
.social .icons i{width:26px;height:26px;border-radius:50%;background:#2f7fc4}
.copyright{position:absolute;left:0;top:3195px;width:1200px;text-align:center;font:400 9px "Open Sans",sans-serif;color:var(--muted)}
</style>
</head>
<body>

<header class="site-header">
  <div class="brand"><div class="brand-mark">TMVB</div><div class="brand-name">Tremont Vale Brokers</div></div>
  <nav class="main-nav"><span>HOME</span><span>SERVICES</span><span>ABOUT TMVB</span><span>CONTACT US</span><span>BLOG</span><span>MARKET NEWS</span></nav>
  <div class="call-btn"><small>Call Today</small><b>214-555-0142</b></div>
</header>

<section class="hero" role="img" aria-label="Photo of the Dallas skyline above green parkland">
  <div class="arrow" style="left:85px"></div>
  <div class="arrow" style="left:1073px"></div>
  <h1>Professional office and warehouse leasing</h1>
  <p>Fast-track your search with tenant reps that only serve you, and specialize in the DFW area.</p>
  <div class="btn">VIEW DETAILS</div>
</section>

<h2 class="section-title" style="top:605px">Why <span>Tenant Representation?</span></h2>

<div class="feature" style="left:125px;top:660px">
  <div class="ico"><svg width="22" height="22" viewBox="0 0 24 24" fill="none" stroke="#d8413a" stroke-width="1.6"><path d="M2 12l5-5 5 3 5-3 5 5-5 5-5-3-5 3z"/></svg></div>
  <h3>Relationships</h3>
  <p>Save time by trusting TMVB year after year to find the right location for you. Over time we've worked together.</p>
</div>
<div class="feature" style="left:390px;top:660px">
  <div class="ico"><svg width="20" height="22" viewBox="0 0 20 24" fill="none" stroke="#d8413a" stroke-width="1.6"><path d="M3 2h10l4 4v16H3z"/><path d="M6 10h8M6 14h8M6 18h5"/></svg></div>
  <h3>Access to more:</h3>
  <p>We have no agreements or personal incentives for specific properties, so we can always show you the offices that are right for you.</p>
</div>
<div class="feature" style="left:125px;top:828px">
  <div class="ico"><svg width="22" height="22" viewBox="0 0 24 24" fill="none" stroke="#d8413a" stroke-width="1.6"><circle cx="12" cy="12" r="9"/><path d="M15 8.5c-1-1-5-1.5-5 1s5 1.5 5 4-4 2.5-5.5 1M12 5.5v13"/></svg></div>
  <h3>Free to you</h3>
  <p>You pay us nothing. We get our commission from the property being leased.</p>
</div>
<div class="feature" style="left:390px;top:828px">
  <div class="ico"><svg width="22" height="22" viewBox="0 0 24 24" fill="none" stroke="#d8413a" stroke-width="1.6"><circle cx="12" cy="12" r="3"/><path d="M12 3v3M12 18v3M3 12h3M18 12h3M5.6 5.6l2.1 2.1M16.3 16.3l2.1 2.1M5.6 18.4l2.1-2.1M16.3 7.7l2.1-2.1"/></svg></div>
  <h3>Customized service</h3>
  <p>Aside from saving you the time of repeating what your needs are to each new location, we also provide a report of the places you've seen.</p>
</div>

<div class="house-side" style="left:710px;top:770px;width:60px;height:160px"></div>
<div class="house-side" style="left:985px;top:708px;width:63px;height:245px"></div>
<div class="house-photo" role="img" aria-label="Photo of a white two-storey house with a green lawn"></div>
<div class="house-frame"></div>

<section class="band band-cta">
  <div class="inner-frame"></div>
  <p>If you need to find office or warehouse space in the Dallas Fort Worth area,<br>the team at TMVB has the experience you need.</p>
  <div class="btn">Space Calculator</div>
</section>

<h2 class="section-title" style="top:1326px">Meet <span>the Team</span></h2>
<p class="intro">At TMVB we believe that you deserve the best professional advice and personal service with your commercial real estate negotiations. By choosing TMVB as your tenant reps in the Dallas/Fort Worth area, you will receive the assistance of accomplished and experienced commercial real estate brokers and salespeople who are licensed by the Lone Star Realty Board to practice in Texas since 1982.</p>

<div class="member" style="left:133px">
  <div class="photo" role="img" aria-label="Portrait of the founder in a dark suit" style="background:linear-gradient(180deg,#cfe0ec,#2e3b4a)"></div>
  <h4>Graham H. Whitlow</h4><em>Founder and President</em>
</div>
<div class="member" style="left:464px">
  <div class="photo" role="img" aria-label="Portrait of the senior director in a grey suit" style="background:linear-gradient(180deg,#f0f0f0,#3a3d42);border-radius:0"></div>
  <h4>Mark Penrose-Hale</h4><em>Senior Director, Commercial Property Specialist</em>
</div>
<div class="member" style="left:795px">
  <div class="photo" role="img" aria-label="Portrait of the associate in a grey suit" style="background:linear-gradient(180deg,#d6ddd9,#4a4f55)"></div>
  <h4>Michael Andrew Reyes</h4><em>Jr., Associate, Tenant Rep Specialist</em>
</div>

<section class="band band-quote">
  <div class="kicker">Look at our</div>
  <h3>Client Testimonials</h3>
  <div class="avatar" role="img" aria-label="Client portrait"></div>
  <div class="who">Curtis Brandon Dale<small>Dallas TX</small></div>
  <blockquote>"The real estate team at TMVB has decades of experience in Commercial. One advantage of TMVB is they know of the properties that are about to become available BEFORE they are available. They have the inside track on properties and they watch your back at the negotiating table. Very impressive with a polished approach. Let the team run with your next project and you won't be disappointed."</blockquote>
  <div class="dots"><i></i><i></i><i></i><i></i></div>
</section>

<p class="appt">Whether your lease is expiring soon, or you're just starting your search,<br>TMVB can help you find the perfect space.</p>
<div class="appt-btn">- MAKE AN APPOINTMENT -</div>

<h2 class="section-title" style="top:2352px">Recent <span>Articles</span></h2>
<div class="article" style="left:135px">
  <div class="thumb" role="img" aria-label="Photo of a hand holding a small house model" style="background:linear-gradient(135deg,#2a3d5c,#8a9bb0)"></div>
  <h5>Image – Minus id quod</h5>
  <p>Lorem Ipsum as their default model text, and publishing packages and web page editors now use Lorem Ipsum as their default model text, and a</p>
  <a>read more</a>
</div>
<div class="article" style="left:458px">
  <div class="thumb" role="img" aria-label="Photo of a house model on rolled blueprints" style="background:linear-gradient(135deg,#f2f2f2,#c8b9a4)"></div>
  <h5>Image – Minus id quod</h5>
  <p>Lorem Ipsum as their default model text, and publishing packages and web page editors now use Lorem Ipsum as their default model text, and a</p>
  <a>read more</a>
</div>
<div class="article" style="left:785px;top:2390px">
  <div class="thumb" role="img" aria-label="Photo of a hand placing a wooden house in a sunny field" style="background:linear-gradient(180deg,#f1a52a,#8aa53a 60%,#4d7a26)"></div>
  <h5>Image – Minus id quod</h5>
  <p>Lorem Ipsum as their default model text, and publishing packages and web page editors now use Lorem Ipsum as their default model text, and a</p>
  <a>read more</a>
</div>

<div class="skyline-fade" role="img" aria-label="Faint Dallas skyline backdrop"></div>

<div class="find">
  <h3>It's easy to <span>find us</span></h3>
  <p>Lorem Ipsum as their default model text, and publishing packages and web page editors now use Lorem Ipsum as their default model text, and a search for 'lorem ipsum' will uncover many</p>
</div>
<div class="info" style="top:2878px"><div class="dot"><svg width="14" height="18" viewBox="0 0 14 18" fill="#fff"><path d="M7 0a7 7 0 0 0-7 7c0 5 7 11 7 11s7-6 7-11a7 7 0 0 0-7-7zm0 10a3 3 0 1 1 0-6 3 3 0 0 1 0 6z"/></svg></div><span>410 Cedar Row Suite 210,<br>Dallas, TX 75201</span></div>
<div class="info" style="top:2945px"><div class="dot"><svg width="16" height="16" viewBox="0 0 24 24" fill="none" stroke="#fff" stroke-width="2"><path d="M5 3h4l2 5-3 2a11 11 0 0 0 6 6l2-3 5 2v4a2 2 0 0 1-2 2A18 18 0 0 1 3 5a2 2 0 0 1 2-2z"/></svg></div><span>214-555-0142</span></div>
<div class="info" style="top:3010px"><div class="dot"><svg width="16" height="16" viewBox="0 0 24 24" fill="none" stroke="#fff" stroke-width="2"><rect x="5" y="3" width="14" height="6"/><rect x="3" y="9" width="18" height="9"/><rect x="7" y="15" width="10" height="6"/></svg></div><span>214-555-0187</span></div>
<ul class="notices">
  <li><b>*</b> Lone Star Realty Board Mandated Disclosure Notices</li>
  <li class="sub">Lone Star Realty Board Information About Brokerage Services</li>
  <li class="sub">Lone Star Realty Board Consumer Protection Notice</li>
</ul>

<div class="contact"><h3>Contact <span>us</span></h3></div>
<div class="field" style="left:612px;top:2793px;width:213px;height:45px">Your Name</div>
<div class="field" style="left:842px;top:2793px;width:225px;height:45px">Phone Number</div>
<div class="field" style="left:612px;top:2858px;width:455px;height:130px">Message</div>
<div class="send">SEND</div>

<div class="social">
  <h3>Social <span>links</span></h3>
  <div class="icons"><i></i><i style="background:#3aa6e6"></i><i style="background:#d8413a"></i><i style="background:#2a79b0"></i></div>
</div>

<p class="copyright">© 2007-2016 TMVB tmvb-realty.example. All rights reserved.</p>

</body>
</html>
```